Indian Takeaway Menu -

I would like to have double parallel fold A4 sheet menu.
A4 sheet cut in half and attached to the other half to make the sheet 4 small pages long.

Colors
abd036
ffffff

Requirements
Must have
• Please check new attachments - menu size and layout is not correct.
• I would like to add Dark brown colour. A4 sheet folded 4x Menu layout pocket size.
Nice to have
• Dark Brown - Parrot Green and very light Brown

```html
<!DOCTYPE html>
<html lang="en">
<head>
<meta charset="utf-8">
<title>Saffron Hearth – Takeaway Menu</title>
<link href="https://fonts.googleapis.com/css2?family=Open+Sans:ital,wght@0,400;0,600;0,700;1,700;1,800&family=Sansita:ital,wght@1,700;1,800&display=swap" rel="stylesheet">
<style>
:root{
  --green:#abd036;
  --green-deep:#8fb322;
  --white:#ffffff;
  --ink:#2e2218;
  --brown:#4a3322;
  --brown-light:#c9a77f;
  --backdrop:#e3e3e3;
  --pad-y:12px;
  --pad-x:14px;
}
*{box-sizing:border-box;margin:0;padding:0}
html,body{width:1200px;height:1200px;overflow:hidden}
body{background:var(--backdrop);font-family:"Open Sans",Arial,sans-serif;color:var(--ink);position:relative}
.sheet{position:absolute;left:30px;width:1140px;height:570px;display:flex;box-shadow:0 6px 18px rgba(0,0,0,.18)}
.sheet--outside{top:20px}
.sheet--inside{top:610px}
.panel{width:285px;height:100%;padding:var(--pad-y) var(--pad-x);position:relative;overflow:hidden;display:flex;flex-direction:column}
.panel--green{background:var(--green)}
.panel--white{background:var(--white)}
.section-title{background:var(--green);color:var(--white);font-family:"Sansita",Georgia,sans-serif;font-style:italic;font-weight:800;font-size:14px;text-align:center;padding:1px 0;margin:3px 0 6px;letter-spacing:.5px}
.panel--green .section-title{background:transparent;border:1.5px solid var(--white);color:var(--white)}
.item{margin-bottom:4px}
.item__row{display:flex;align-items:baseline;font-size:9px;font-weight:800;font-style:italic;line-height:1.25}
.item__row .lead{flex:1;border-bottom:1px dotted currentColor;margin:0 3px;transform:translateY(-2px)}
.item__row .price{font-style:normal;font-weight:700}
.item__desc{font-size:7.5px;line-height:1.2}
.item--tight{margin-bottom:3px}
.price-list{font-size:8.5px;line-height:1.45}
.price-list .item__row{font-weight:600;font-style:normal;font-size:8.5px;line-height:1.45}
.allergens{background:var(--green);padding:6px 10px;margin-top:14px}
.allergens h3{text-align:center;font-size:10px;font-weight:700;margin-bottom:3px}
.allergens ul{list-style:none;columns:2;font-size:8.5px;line-height:1.3}
.hours-photo{position:absolute;inset:0;background:linear-gradient(180deg,#ffffff 0%,#f3efe9 32%,#b58a62 55%,#6b4a33 78%,#3b2a1d 100%)}
.hours{position:relative;z-index:1;padding-top:24px;text-align:center}
.hours__box{border:2px solid var(--green);padding:8px 6px;font-size:9.5px;line-height:1.5}
.hours__box h3{font-size:13px;font-weight:700;letter-spacing:1.5px;margin-bottom:3px}
.call{margin-top:18px;font-size:13px;font-weight:600;line-height:1.25}
.call small{display:block;font-size:9px;font-weight:600;margin-top:4px}
.cover-photo{height:175px;margin:calc(-1*var(--pad-y)) calc(-1*var(--pad-x)) 0;background:radial-gradient(circle at 35% 40%,#e8a43a 0%,#c96a2a 35%,#8c3b22 65%,#4a3322 100%)}
.brand{display:flex;align-items:center;justify-content:center;gap:8px;margin-top:30px}
.brand__mark{width:14px;height:14px;background:var(--green)}
.brand__name{font-family:"Open Sans",Arial,sans-serif;font-weight:700;font-size:22px;color:var(--ink)}
.brand__tag{text-align:center;font-size:7.5px;letter-spacing:1px;margin-top:2px}
.badge{width:86px;height:86px;border-radius:50%;background:var(--green);margin:30px auto 0}
.cover-note{text-align:center;font-size:9px;margin-top:auto;margin-bottom:6px}
.cover-web{background:var(--green);color:var(--ink);text-align:center;font-weight:700;font-size:11px;padding:6px;margin:0 calc(-1*var(--pad-x)) 24px}
.deal-title{border:1.5px solid var(--white);color:var(--white);text-align:center;font-family:"Sansita",Georgia,sans-serif;font-style:italic;font-weight:800;font-size:14px;padding:1px;margin-top:3px}
.deal-sub{text-align:center;font-size:8px;font-weight:700;font-style:italic;margin:4px 0 6px;line-height:1.3}
.set-list{font-size:7.5px;line-height:1.2;padding-left:6px}
.pakora-photo{margin:auto calc(-1*var(--pad-x)) calc(-1*var(--pad-y));height:120px;flex-shrink:0;background:radial-gradient(circle at 55% 55%,#e6b45a 0%,#c68a3a 40%,#8a6a44 75%,#5a4a36 100%)}
.key{border:1px solid var(--green);padding:3px 8px;font-size:8px;line-height:1.3;margin:2px auto 4px;width:80%}
.panel--white .item{border-bottom:1px solid rgba(171,208,54,.6);padding-bottom:2px}
</style>
</head>
<body>

<section class="sheet sheet--outside" aria-label="Menu outside">
  <div class="panel panel--green">
    <div class="item"><div class="item__row">Lamb Jalfrezi 2,5<span class="lead"></span><span class="price">€10.95</span></div><div class="item__desc">Lamb cooked with chunks of onions, peppers and fresh green chillies.</div></div>
    <div class="item"><div class="item__row">Goshi Biryani 3,5 (y)<span class="lead"></span><span class="price">€11.00</span></div><div class="item__desc">Aged basmati rice cooked with tender lamb and dry spices, served with curry sauce.</div></div>
    <div class="section-title">Prawn Dishes</div>
    <div class="item"><div class="item__row">Prawn Masala 3<span class="lead"></span><span class="price">€11.95</span></div><div class="item__desc">Prawns in a creamy tomato sauce with kasoori methi.</div></div>
    <div class="item"><div class="item__row">Prawn Karahi<span class="lead"></span><span class="price">€11.95</span></div><div class="item__desc">Prawns tossed with peppers, onion and whole spices.</div></div>
    <div class="item"><div class="item__row">Goan Prawn Curry 3,4,5<span class="lead"></span><span class="price">€11.95</span></div><div class="item__desc">Fresh prawns in coconut and tamarind coastal sauce.</div></div>
    <div class="item"><div class="item__row">Prawn Bhuna 3<span class="lead"></span><span class="price">€11.95</span></div><div class="item__desc">Prawns with tomatoes, onions and black pepper.</div></div>
    <div class="item"><div class="item__row">Prawn Biryani 3,5 (y)<span class="lead"></span><span class="price">€11.95</span></div><div class="item__desc">Basmati rice with prawns, served with curry sauce.</div></div>
    <div class="section-title">Vegetarian Dishes</div>
    <div class="item"><div class="item__row">Shahi Paneer 3,5<span class="lead"></span><span class="price">€8.95</span></div><div class="item__desc">Indian cheese in a rich semi-dry sauce.</div></div>
    <div class="item"><div class="item__row">Subz Malai Mild 3<span class="lead"></span><span class="price">€8.95</span></div><div class="item__desc">Stir fried vegetables with ground spices.</div></div>
    <div class="item"><div class="item__row">Dum Wale Aloo 3<span class="lead"></span><span class="price">€8.95</span></div><div class="item__desc">Potatoes cooked with ginger, garlic and yoghurt.</div></div>
    <div class="item"><div class="item__row">Karahi Paneer 3 (y)<span class="lead"></span><span class="price">€8.95</span></div><div class="item__desc">Paneer prepared using homemade Indian spices.</div></div>
    <div class="item"><div class="item__row">Saag Paneer 3<span class="lead"></span><span class="price">€8.95</span></div><div class="item__desc">Pan fried cottage cheese &amp; spinach with methi.</div></div>
  </div>

  <div class="panel panel--white">
    <div class="section-title">Nan Bread &amp; Side Orders</div>
    <p style="text-align:center;font-size:8px;font-weight:700;margin-bottom:4px">All naan bread contains 2,3,6</p>
    <div class="price-list">
      <div class="item__row">Naan<span class="lead"></span><span class="price">€2.70</span></div>
      <div class="item__row">Garlic Naan<span class="lead"></span><span class="price">€2.90</span></div>
      <div class="item__row">Garlic Chilli Naan<span class="lead"></span><span class="price">€3.00</span></div>
      <div class="item__row">Peshwari Naan 5<span class="lead"></span><span class="price">€3.00</span></div>
      <div class="item__row">Keema Naan<span class="lead"></span><span class="price">€3.00</span></div>
      <div class="item__row">Coriander Naan 3<span class="lead"></span><span class="price">€2.50</span></div>
      <div class="item__row">Chilli Cheese Naan<span class="lead"></span><span class="price">€3.00</span></div>
      <div class="item__row">G.O.C.<span class="lead"></span><span class="price">€2.80</span></div>
      <div class="item__row">Boiled Basmati<span class="lead"></span><span class="price">€2.00</span></div>
      <div class="item__row">Pilau Rice<span class="lead"></span><span class="price">€3.00</span></div>
      <div class="item__row">Lemon Rice 4<span class="lead"></span><span class="price">€3.00</span></div>
      <div class="item__row">Poppadum(2)<span class="lead"></span><span class="price">€2.50</span></div>
      <div class="item__row">Raita 3<span class="lead"></span><span class="price">€2.50</span></div>
    </div>
    <div class="allergens">
      <h3>Allergens</h3>
      <ul>
        <li>Eggs</li><li>Nuts</li><li>Mustard</li><li>Crustaceans</li><li>Soya</li><li>Fish</li><li>Gluten</li>
        <li>Milk / Yoghurt</li><li>Sesame Seeds</li><li>Celery</li><li>Lupin</li><li>Peanuts</li><li>Molluscs</li><li>Sulphur dioxide</li>
      </ul>
    </div>
  </div>

  <div class="panel panel--white">
    <div class="hours-photo" role="img" aria-label="Photo of whole spices, dried red chillies and peppercorns on a rustic wooden table"></div>
    <div class="hours">
      <div class="hours__box">
        <h3>OPENING HOURS</h3>
        Sun - Thurs 5PM to 10.00PM<br>
        Fri - Sat 5.00PM-10.30PM<br>
        Deliveries From 5.30PM
      </div>
      <div class="call">Call Now<br>015550142<br>015550143<small>www.saffronhearth.ie</small></div>
    </div>
  </div>

  <div class="panel panel--white">
    <div class="cover-photo" role="img" aria-label="Photo of a colourful vegetable curry with fresh coriander and red chillies"></div>
    <div class="brand"><span class="brand__mark"></span><span class="brand__name">Saffron Hearth</span></div>
    <p class="brand__tag">AUTHENTIC INDIAN FOOD TO ORDER</p>
    <div class="badge" role="img" aria-label="Green natural food badge"></div>
    <p class="cover-note">All our meals are cooked to order.</p>
    <div class="cover-web">www.saffronhearth.ie</div>
  </div>
</section>

<section class="sheet sheet--inside" aria-label="Menu inside">
  <div class="panel panel--green">
    <div class="deal-title">Meal Deals only €8.50</div>
    <p class="deal-sub">(Low Fat Dishes)<br>Choose with Rice or Plain Naan</p>
    <div class="item item--tight"><div class="item__row">Chicken Dupiaza<span class="lead"></span><span class="price">8.50</span></div><div class="item__desc">Chicken cooked with ginger and chunks of onions, finished with onion seeds.</div></div>
    <div class="item item--tight"><div class="item__row">Chicken Rogan Josh<span class="lead"></span><span class="price">8.50</span></div><div class="item__desc">A red chicken curry with fresh herb &amp; spices, a delicacy from Kashmir.</div></div>
    <div class="item item--tight"><div class="item__row">Chicken Bhuna<span class="lead"></span><span class="price">8.50</span></div><div class="item__desc">Tomatoes and onion sauce cooked with black peppers &amp; spring onions.</div></div>
    <div class="item item--tight"><div class="item__row">Tarkari Makhani 3,5<span class="lead"></span><span class="price">8.50</span></div><div class="item__desc">Mixed seasonal vegetables in a smooth tikka masala sauce.</div></div>
    <div class="item item--tight"><div class="item__row">Set Meal 1<span class="lead"></span><span class="price">€16.00</span></div><div class="set-list">- Onion Bhajia<br>- Chicken Tikka Masala<br>- Pilau rice<br>- Naan<br>- Poppadoms</div></div>
    <div class="item item--tight"><div class="item__row">Set Meal For 2<span class="lead"></span><span class="price">€27.00</span></div><div class="set-list">- Onion bhajia - Chicken tikka<br>- Chicken Tikka Masala - Lamb Roganjosh<br>- 2xPilau rice - 1xNaan - Poppadom</div></div>
    <div class="item item--tight"><div class="item__row">Set Meal for 3/4<span class="lead"></span><span class="price">€43.00</span></div><div class="set-list">- Onion bhajia - Vegetable samosa<br>- Chicken tikka - Chicken Tikka Masala<br>- Lamb Roganjosh - Sambhar Veg Curry<br>- 2 x Pilau Rice - 2 x Naan - Poppadom</div></div>
    <div class="pakora-photo" role="img" aria-label="Photo of golden vegetable pakoras on a white plate"></div>
  </div>

  <div class="panel panel--white">
    <div class="section-title">Healthy Side orders</div>
    <div class="item"><div class="item__row">Sautéed Broccoli (v)<span class="lead"></span><span class="price">€5.00</span></div><div class="item__desc">Broccoli, green beans and spinach leaves sautéed with roasted cumin and fresh garlic.</div></div>
    <div class="item"><div class="item__row">Chana Saag 3 (y)(v)<span class="lead"></span><span class="price">€5.00</span></div><div class="item__desc">Chickpeas cooked with chopped spinach, onion, and cumin and finished with cream.</div></div>
    <div class="item"><div class="item__row">Chana Masala (v)<span class="lead"></span><span class="price">€5.00</span></div><div class="item__desc">Chickpeas simmered with tomato, caramelised onion, black pepper and fresh coriander.</div></div>
    <div class="item"><div class="item__row">Aloo Saag 3 (y)(v)<span class="lead"></span><span class="price">€5.00</span></div><div class="item__desc">Crispy Potato with spinach, caramelised onion, garam masala and a dash of cream.</div></div>
    <div class="item"><div class="item__row">Aloo Ghobhi (v)<span class="lead"></span><span class="price">€5.00</span></div><div class="item__desc">Crispy Potatoes cubes &amp; Cauliflower cooked with roasted cumin with tomato and onion gravy.</div></div>
    <div class="item"><div class="item__row">Tarka Daal 4 (y)(v)<span class="lead"></span><span class="price">€5.00</span></div><div class="item__desc">Home style soaked yellow chana cooked with cumin &amp; garam masala.</div></div>
    <div class="item"><div class="item__row">Tangy Aloo (v)<span class="lead"></span><span class="price">€5.00</span></div><div class="item__desc">Crispy Potatoes cubes cooked with roasted cumin and touch of our tangy sauce.</div></div>
    <div class="key">Y: Can be cooked without allergen<br>H: Healthy Option<br>V: Suitable for Vegans</div>
    <div class="section-title">Starters</div>
    <div class="item"><div class="item__row">Onion Bhajia<span class="lead"></span><span class="price">€4.50</span></div><div class="item__desc">Spinach &amp; onions fritters flavored with mild spices.</div></div>
    <div class="item"><div class="item__row">Vegetable Samosa 2<span class="lead"></span><span class="price">€4.50</span></div><div class="item__desc">Crispy Pastry stuffed with potatoes, chick peas, green peas mixed with desi spices.</div></div>
    <div class="item"><div class="item__row">Palak Tikki<span class="lead"></span><span class="price">€4.50</span></div><div class="item__desc">Cakes of fresh spinach and chana dal.</div></div>
    <div class="item"><div class="item__row">Veg Pakora<span class="lead"></span><span class="price">€5.00</span></div><div class="item__desc">Cauliflower, potato and broccoli, golden fried with gram flour batter.</div></div>
    <div class="item"><div class="item__row">Keema Singhara 2<span class="lead"></span><span class="price">€5.00</span></div><div class="item__desc">Spicy seasoned mince lamb in light pastry.</div></div>
  </div>

  <div class="panel panel--green">
    <div class="item item--tight"><div class="item__row">Chicken Tikka 3<span class="lead"></span><span class="price">€5.00</span></div><div class="item__desc">Tender chicken marinated overnight with yoghurt, spices charred in tandoor.</div></div>
    <div class="item item--tight"><div class="item__row">Seekh Kebab<span class="lead"></span><span class="price">€5.50</span></div><div class="item__desc">Skewered hand pounder lamb glazed in tandoor with green chilli &amp; black cardamom.</div></div>
    <div class="item item--tight"><div class="item__row">Chicken Pakora<span class="lead"></span><span class="price">€5.00</span></div><div class="item__desc">Boneless pieces of chicken coated in gram flour batter, with spices.</div></div>
    <div class="item item--tight"><div class="item__row">Chicken Wings 2,1<span class="lead"></span><span class="price">€5.00</span></div></div>
    <div class="item item--tight"><div class="item__row">Tandoori Mix Meat Platter 3<span class="lead"></span><span class="price">€9.50</span></div><div class="item__desc">Our special tandoori assortment of tandoori chicken on bone, seekh kebab and chicken tikka.</div></div>
    <div class="item item--tight"><div class="item__row">Mix Veg platter 2<span class="lead"></span><span class="price">€6.50</span></div><div class="item__desc">Veg Samosa, Onion Bhaji, Veg Pakora.</div></div>
    <div class="item item--tight"><div class="item__row">Doner Kebab 2,3,6<span class="lead"></span><span class="price">€8.00</span></div><div class="item__desc">Stripes of minced chicken &amp; beef served with garlic mayo, chilli sauce &amp; mixed salad &amp; wrapped in naan.</div></div>
    <div class="item item--tight"><div class="item__row">Chicken Tikka Kebab 2,3,6<span class="lead"></span><span class="price">€8.00</span></div><div class="item__desc">Chicken breast marinated in spices, barbecued served with garlic mayo, chilli sauce &amp; mixed salad &amp; wrapped in naan.</div></div>
    <div class="item item--tight"><div class="item__row">Mix Kebab 2,3,6<span class="lead"></span><span class="price">€8.00</span></div><div class="item__desc">Pieces of chicken tikka &amp; donner meat with garlic mayo, sweet chilli &amp; salad wrapped in naan bread.</div></div>
    <div class="item item--tight"><div class="item__row">Garlic Chips<span class="lead"></span><span class="price">€4.00</span></div></div>
    <div class="section-title" style="font-size:13px">Chef Arun's Special Curries</div>
    <div class="item item--tight"><div class="item__row">Butter Murgh 3,5<span class="lead"></span><span class="price">€10.50</span></div><div class="item__desc">Chicken cooked in tandoor mixed with rich tomato creamy cashew sauce, splash of cream with hint of honey &amp; dry fenugreek.</div></div>
    <div class="item item--tight"><div class="item__row">Laal Maas<span class="lead"></span><span class="price">€11.50</span></div><div class="item__desc">Tadionnal rajasthani lamb cooked with garlic and ginger, degi chilli powder, tomatoes finished with star aniseed and clove powder.</div></div>
    <div class="item item--tight"><div class="item__row">Shahi Veg Kofta 3,5<span class="lead"></span><span class="price">€10.00</span></div><div class="item__desc">Handmade veg and paneer dumplings simmered in tomato sauce, finished with touch of honey and cream.</div></div>
    <div class="item item--tight"><div class="item__row">Kerala Prawn 14<span class="lead"></span><span class="price">€12.00</span></div><div class="item__desc">Delicacy of kerala spices, tomato and red onion gravy finished with touch of fresh coconut milk.</div></div>
  </div>

  <div class="panel panel--white">
    <div class="section-title">Chicken Dishes</div>
    <div class="item"><div class="item__row">Punjabi Saag 3 (y)<span class="lead"></span><span class="price">€9.95</span></div><div class="item__desc">Chicken cooked with spinach, ginger, garlic, fresh cream &amp; temperd with Punjabi tarka.</div></div>
    <div class="item"><div class="item__row">Royale Korma 3,5<span class="lead"></span><span class="price">€8.95</span></div><div class="item__desc">Breast of chicken cooked in a rich creamy sauce with saffron &amp; coconut, probably most popular among Irish.</div></div>
    <div class="item"><div class="item__row">Saffron Hearth Chicken Curry 3,4,5<span class="lead"></span><span class="price">€8.95</span></div><div class="item__desc">Traditional curry cooked with coconut, mustard seed, cashews and curry leaves.</div></div>
    <div class="item"><div class="item__row">Chicken Karahi<span class="lead"></span><span class="price">€8.95</span></div><div class="item__desc">Boneless chicken prepared in Deg with peppers, onion, tomatoes and Indian whole spices.</div></div>
    <div class="item"><div class="item__row">Chicken Tikka Masala 3<span class="lead"></span><span class="price">€8.95</span></div><div class="item__desc">Chicken roasted in clayoven and simmered in smooth creamy tomato sauce with palm crushed fenugreek leaves and jiggery.</div></div>
    <div class="item"><div class="item__row">South Indian Garlic Chilli<span class="lead"></span><span class="price">€8.95</span></div><div class="item__desc">Chicken cooked in south Indian style and loaded with garlic, ground spices, fresh herbs.</div></div>
    <div class="item"><div class="item__row">Chicken Dahiwala 3<span class="lead"></span><span class="price">€8.95</span></div><div class="item__desc">Amazingly spicy chicken curry cooked with yogurt, green chillies, ginger and herbs.</div></div>
    <div class="item"><div class="item__row">Murgh Biryani 3,5 (y)<span class="lead"></span><span class="price">€9.95</span></div><div class="item__desc">Perfumed basmati rice with chicken cubes, nuts, golden onions and biryani spices, served with sauce.</div></div>
    <div class="section-title">Lamb Dishes</div>
    <div class="item"><div class="item__row">Lamb Madras<span class="lead"></span><span class="price">€10.95</span></div><div class="item__desc">The popular dish of madras cooked with plum tomato, degi chilli, coconut and finished with hint of lemon juice.</div></div>
    <div class="item"><div class="item__row">Palak Gosht 3 (y)<span class="lead"></span><span class="price">€10.95</span></div><div class="item__desc">Pan fried lamb pieces cooked with spinach, fresh herbs, ginger and touch of cream.</div></div>
    <div class="item"><div class="item__row">Lamb Roganjosh<span class="lead"></span><span class="price">€10.95</span></div><div class="item__desc">Slow cooked tender lamb in kashmiri style with fresh herbs and Himalayan spices.</div></div>
    <div class="item"><div class="item__row">Lamb Kohlapuri 3,4,5<span class="lead"></span><span class="price">€10.95</span></div><div class="item__desc">Lamb dish from South Coast of India flavoured with yoghurt, nuts and coconut.</div></div>
  </div>
</section>

</body>
</html>
```